Private Equity Fund needs a powerpoint template

We need a power point presentation template for our recent founded firm, Corvane Partners, a private equity/investment fund (funded by investors, is a firm that buys, holds and sells companies years after) focused in turnaround cases. The presentation should address corporate and financial subjects in a clean/plain way, but as most straightforward way as possible. This is a commercial pitch/flip presentation, is not a presentation with animations to be presented to a mass of people.

We would like that the designer resume the file that we began building (adapted from other funds/advisors of the market) and establish the following according to our logo:
1) a new set of fonts (size levels and type),
2) colors (tables, headers, lines),
3) space available for content (text boxes, tables, pictures or charts) (note left column space in blank)
4) set, our Excel applications to use as default, the color guide that you have you defined
5) white background

Basically, we need to change the items listed above to the "Example.ppt" file uploaded along with those instructions.

The presentation should:
A) rule how the people in our organization should address our messages (guide with size of tables, font and size, colors)
B) pattern a set of slides that could minimize the time for arranging formats, worrying only about the content
C) allow the person who is building the presentation to have options while addressing the message

Dont get too restricted to what we are giving you (the "Example.ppt" file). You may suggest:
i) logo positioning
ii) with or without any vague space (left column space in blank)
iii) space optmization
iv) shades and colors
v) fonts (careful with the wide ones as it does not optimizes space)

I'm uploading:

Target Market(s)

Banks
Investors
Company owners/founders
Funds

Industry/Entity Type

Financial Service

Font styles to use
Other font styles liked:
• Arial Narrow, Arial, trojan

Colors

Designer to choose colors to be used in the design.

Requirements
Must have
• We would like that the designer resume the file that we began building (adapted from other funds/advisors of the market) and establish the following according to our logo:
• 1) a new set of fonts (size levels and type),
• 2) colors (tables, headers, lines),
• 3) space available for content (text boxes, tables, pictures or charts) (note left column space in blank)
• 4) set, our Excel applications to use as default, the color guide that you have you defined
• 5) white background
Nice to have
• Narrow font type
• Space optimization
• Discrete
Should not have
• Animations
• Font size too big
• colored background

```html
<!DOCTYPE html>
<html lang="en">
<head>
<meta charset="utf-8">
<title>Corvane Partners – Presentation Template Overview</title>
<link href="https://fonts.googleapis.com/css2?family=Archivo+Narrow:wght@400;600&display=swap" rel="stylesheet">
<style>
:root{
  --page:#e6e6e6;
  --paper:#ffffff;
  --ink:#4a4d55;
  --muted:#8b8e96;
  --rule:#c9ccd2;
  --slate:#8b93a6;
  --slate-dark:#6f778c;
  --purple:#837b98;
  --olive:#9b9574;
  --brown:#8f806a;
  --sage:#a6b39a;
  --sage-light:#d6decb;
  --rose:#b8a3aa;
  --light:#dfe2e8;
  --pale:#eef0f3;
}
*{box-sizing:border-box;margin:0;padding:0}
html,body{width:1200px;height:3003px;overflow:hidden;background:var(--page)}
body{font-family:"Archivo Narrow","Arial Narrow",Arial,sans-serif;color:var(--ink)}
.deck{display:grid;grid-template-columns:repeat(3,394px);grid-auto-rows:292px;gap:9px;padding-top:1px}
.slide{position:relative;background:var(--paper);overflow:hidden}
.slide-no{position:absolute;top:8px;right:10px;width:13px;height:11px;background:var(--slate);color:#fff;font-size:6px;line-height:11px;text-align:center}
.slide-title{position:absolute;left:22px;top:16px;font-size:13px;font-weight:400;text-transform:uppercase;letter-spacing:.2px;color:var(--ink)}
.slide-title.sentence{text-transform:none}
.slide-sub{position:absolute;left:22px;top:33px;font-size:6.5px;text-transform:uppercase;color:var(--muted)}
.content{position:absolute;left:22px;top:48px;width:350px;height:195px}
.strapline{position:absolute;left:22px;top:252px;font-size:8.5px;color:var(--ink)}
.brand-mini{position:absolute;left:10px;bottom:8px;display:flex;align-items:center;gap:4px;font-size:8px;letter-spacing:1.2px;color:var(--muted);text-transform:uppercase}
.brand-mini i,.brand i{display:inline-block;background:var(--muted)}
.brand-mini i{width:8px;height:8px}
.brand{display:flex;align-items:center;gap:8px;color:var(--slate-dark);text-transform:uppercase;letter-spacing:2px}
.brand i{background:var(--slate-dark)}
.cover .brand{position:absolute;left:34px;top:92px;font-size:20px}
.cover .brand i{width:22px;height:22px}
.cover-rule{position:absolute;left:34px;top:126px;width:90px;border-top:1px solid var(--rule)}
.cover-title{position:absolute;left:34px;top:138px;font-size:11px;text-transform:uppercase}
.cover-sub{position:absolute;left:34px;top:153px;font-size:6.5px;text-transform:uppercase;color:var(--muted)}
.divider .brand{position:absolute;left:118px;top:108px;font-size:20px}
.divider .brand i{width:22px;height:22px}
.divider-title{position:absolute;left:118px;top:142px;font-size:10px;text-transform:uppercase}
.toc{position:absolute;left:70px;top:60px;width:250px;list-style:none}
.toc li{display:flex;justify-content:space-between;border-bottom:1px solid var(--rule);padding:3px 0 2px;font-size:6.5px;margin-bottom:8px}
.toc b{display:block;font-weight:600}
svg{display:block}
svg text{font-family:"Archivo Narrow","Arial Narrow",Arial,sans-serif;fill:var(--ink)}
.map{position:absolute;left:40px;top:60px;width:310px;height:170px;background:linear-gradient(135deg,#d3d5d9,#c2c5ca);border-radius:40% 30% 45% 35%}
</style>
</head>
<body>
<main class="deck">

<!-- Cover -->
<section class="slide cover">
  <div class="brand"><i></i>Corvane Partners</div>
  <div class="cover-rule"></div>
  <div class="cover-title">Presentation title goes here</div>
  <div class="cover-sub">Your subtitle goes here</div>
</section>

<!-- Contents -->
<section class="slide">
  <div class="slide-no">2</div>
  <h2 class="slide-title sentence">Contents</h2>
  <ol class="toc">
    <li><span><b>Section 1</b>[Enter title]</span><span>3</span></li>
    <li><span><b>Section 2</b>[Enter title]</span><span>8</span></li>
    <li><span><b>Section 3</b>[Enter title]</span><span>13</span></li>
    <li><span><b>Section 4</b>[Enter title]</span><span>17</span></li>
    <li><span><b>Section 5</b>[Enter title]</span><span>22</span></li>
  </ol>
  <div class="brand-mini"><i></i>Corvane</div>
</section>

<!-- 1 Standard width -->
<section class="slide">
  <div class="slide-no">3</div>
  <h2 class="slide-title">1. Standard width layout</h2>
  <div class="slide-sub">Your subtitle goes here</div>
  <svg class="content" viewBox="0 0 350 195">
    <rect x="0" y="0" width="350" height="8" fill="var(--slate)"/>
    <text x="4" y="6" font-size="5" fill="#fff">Chart title</text>
    <rect x="130" y="14" width="5" height="4" fill="var(--slate)"/><text x="137" y="18" font-size="5">Series 1</text>
    <rect x="165" y="14" width="5" height="4" fill="var(--purple)"/><text x="172" y="18" font-size="5">Series 2</text>
    <rect x="200" y="14" width="5" height="4" fill="var(--brown)"/><text x="207" y="18" font-size="5">Series 3</text>
    <line x1="20" y1="170" x2="340" y2="170" stroke="var(--rule)"/>
    <g>
      <rect x="45" y="60" width="12" height="110" fill="var(--slate)"/><rect x="59" y="95" width="12" height="75" fill="var(--purple)"/><rect x="73" y="130" width="12" height="40" fill="var(--brown)"/>
      <rect x="125" y="110" width="12" height="60" fill="var(--slate)"/><rect x="139" y="45" width="12" height="125" fill="var(--purple)"/><rect x="153" y="125" width="12" height="45" fill="var(--brown)"/>
      <rect x="205" y="80" width="12" height="90" fill="var(--slate)"/><rect x="219" y="120" width="12" height="50" fill="var(--purple)"/><rect x="233" y="100" width="12" height="70" fill="var(--brown)"/>
      <rect x="285" y="40" width="12" height="130" fill="var(--slate)"/><rect x="299" y="90" width="12" height="80" fill="var(--purple)"/><rect x="313" y="75" width="12" height="95" fill="var(--brown)"/>
    </g>
    <text x="52" y="180" font-size="5">CATEGORY 1</text><text x="132" y="180" font-size="5">CATEGORY 2</text><text x="212" y="180" font-size="5">CATEGORY 3</text><text x="292" y="180" font-size="5">CATEGORY 4</text>
    <text x="0" y="192" font-size="4.5" fill="var(--muted)">Source: data 2017</text>
  </svg>
  <div class="strapline">A strapline should be placed here</div>
  <div class="brand-mini"><i></i>Corvane</div>
</section>

<!-- 2 Two column -->
<section class="slide">
  <div class="slide-no">4</div>
  <h2 class="slide-title">2 Two column layout</h2>
  <div class="slide-sub">Your subtitle goes here</div>
  <svg class="content" viewBox="0 0 350 195">
    <rect x="0" y="0" width="170" height="8" fill="var(--slate)"/><text x="4" y="6" font-size="5" fill="#fff">Chart title</text>
    <rect x="180" y="0" width="170" height="8" fill="var(--slate)"/><text x="184" y="6" font-size="5" fill="#fff">Contribution / margin</text>
    <line x1="10" y1="160" x2="165" y2="160" stroke="var(--rule)"/>
    <rect x="20" y="50" width="8" height="110" fill="var(--slate)"/><rect x="29" y="80" width="8" height="80" fill="var(--purple)"/><rect x="38" y="110" width="8" height="50" fill="var(--sage)"/>
    <rect x="60" y="90" width="8" height="70" fill="var(--slate)"/><rect x="69" y="40" width="8" height="120" fill="var(--purple)"/><rect x="78" y="120" width="8" height="40" fill="var(--sage)"/>
    <rect x="100" y="70" width="8" height="90" fill="var(--slate)"/><rect x="109" y="100" width="8" height="60" fill="var(--purple)"/><rect x="118" y="60" width="8" height="100" fill="var(--sage)"/>
    <rect x="140" y="30" width="8" height="130" fill="var(--slate)"/><rect x="149" y="85" width="8" height="75" fill="var(--purple)"/><rect x="158" y="95" width="6" height="65" fill="var(--sage)"/>
    <line x1="190" y1="160" x2="345" y2="160" stroke="var(--rule)"/>
    <g>
      <rect x="200" y="90" width="18" height="70" fill="var(--slate)"/><rect x="200" y="60" width="18" height="30" fill="var(--rose)"/><rect x="200" y="45" width="18" height="15" fill="var(--sage)"/>
      <rect x="230" y="100" width="18" height="60" fill="var(--slate)"/><rect x="230" y="70" width="18" height="30" fill="var(--rose)"/><rect x="230" y="50" width="18" height="20" fill="var(--sage)"/>
      <rect x="260" y="80" width="18" height="80" fill="var(--slate)"/><rect x="260" y="55" width="18" height="25" fill="var(--rose)"/><rect x="260" y="40" width="18" height="15" fill="var(--sage)"/>
      <rect x="290" y="110" width="18" height="50" fill="var(--slate)"/><rect x="290" y="85" width="18" height="25" fill="var(--rose)"/><rect x="290" y="70" width="18" height="15" fill="var(--sage)"/>
      <rect x="320" y="95" width="18" height="65" fill="var(--slate)"/><rect x="320" y="65" width="18" height="30" fill="var(--rose)"/><rect x="320" y="50" width="18" height="15" fill="var(--sage)"/>
    </g>
    <polyline points="209,30 239,95 269,60 299,120 329,40" fill="none" stroke="#a0485a" stroke-width="1"/>
    <text x="20" y="170" font-size="4.5">Category 1   Category 2   Category 3   Category 4</text>
    <text x="0" y="185" font-size="4.5" fill="var(--muted)">Source: data 2017</text>
  </svg>
  <div class="strapline">A strapline should be placed here</div>
  <div class="brand-mini"><i></i>Corvane</div>
</section>

<!-- 3 Three columns -->
<section class="slide">
  <div class="slide-no">5</div>
  <h2 class="slide-title">3 Three columns layout</h2>
  <div class="slide-sub">Three column layout with bullet text</div>
  <svg class="content" viewBox="0 0 350 195">
    <g font-size="5">
      <rect x="0" y="0" width="110" height="8" fill="var(--slate)"/><text x="3" y="6" fill="#fff">Figure 1</text><text x="3" y="15">Revenue 2017</text>
      <rect x="120" y="0" width="110" height="8" fill="var(--slate)"/><text x="123" y="6" fill="#fff">Figure 2</text><text x="123" y="15">Revenue 2017</text>
      <rect x="240" y="0" width="110" height="8" fill="var(--slate)"/><text x="243" y="6" fill="#fff">Figure 3</text><text x="243" y="15">Revenue 2017</text>
    </g>
    <g id="pie-a" transform="translate(55,60)">
      <circle r="32" fill="var(--slate)"/>
      <path d="M0,0 L0,-32 A32,32 0 0,1 30,11 Z" fill="var(--purple)"/>
      <path d="M0,0 L30,11 A32,32 0 0,1 -8,31 Z" fill="var(--sage)"/>
      <path d="M0,0 L-8,31 A32,32 0 0,1 -28,15 Z" fill="var(--rose)"/>
    </g>
    <g transform="translate(175,60)">
      <circle r="32" fill="var(--purple)"/>
      <path d="M0,0 L0,-32 A32,32 0 0,1 32,0 Z" fill="var(--slate)"/>
      <path d="M0,0 L32,0 A32,32 0 0,1 0,32 Z" fill="var(--sage)"/>
    </g>
    <g transform="translate(295,60)">
      <circle r="32" fill="var(--sage)"/>
      <path d="M0,0 L0,-32 A32,32 0 0,1 22,23 Z" fill="var(--slate)"/>
      <path d="M0,0 L22,23 A32,32 0 0,1 -20,25 Z" fill="var(--purple)"/>
    </g>
    <g font-size="4.8">
      <text x="0" y="110">• Current share of total revenue</text><text x="0" y="118">• Margin outlook for next period</text><text x="0" y="126">• Availability of credit lines</text><text x="0" y="134">• Restructuring of cost base</text><text x="0" y="142">• Geographic exposure by region</text>
      <text x="120" y="110">• Integration risk – management view</text><text x="120" y="118">• The margin effect</text><text x="120" y="126">• Further equity opportunities</text><text x="120" y="134">• Key operating ratios reviewed</text><text x="120" y="142">• Stability of the order pipeline</text>
      <text x="240" y="110">• Scale of sector consolidation</text><text x="240" y="118">• Business case approved</text><text x="240" y="126">• Project / asset supporting data</text><text x="240" y="134">• Owner alignment reflected</text><text x="240" y="142">• Timeline of exit options</text>
    </g>
  </svg>
  <div class="strapline">A strapline should be placed here</div>
  <div class="brand-mini"><i></i>Corvane</div>
</section>

<!-- 4 Four charts -->
<section class="slide">
  <div class="slide-no">6</div>
  <h2 class="slide-title">4 Four charts on a page</h2>
  <div class="slide-sub">Your subtitle goes here</div>
  <svg class="content" viewBox="0 0 350 195">
    <rect x="0" y="0" width="170" height="7" fill="var(--slate)"/><text x="3" y="5.5" font-size="4.5" fill="#fff">Revenue by unit</text>
    <rect x="180" y="0" width="170" height="7" fill="var(--slate)"/><text x="183" y="5.5" font-size="4.5" fill="#fff">Revenue trend</text>
    <g fill="var(--olive)">
      <rect x="30" y="15" width="70" height="6"/><rect x="30" y="25" width="40" height="6"/><rect x="30" y="35" width="95" height="6"/><rect x="30" y="45" width="55" height="6"/><rect x="30" y="55" width="30" height="6"/><rect x="30" y="65" width="80" height="6"/>
    </g>
    <text x="2" y="20" font-size="4">Unit A</text><text x="2" y="30" font-size="4">Unit B</text><text x="2" y="40" font-size="4">Unit C</text><text x="2" y="50" font-size="4">Unit D</text><text x="2" y="60" font-size="4">Unit E</text><text x="2" y="70" font-size="4">Unit F</text>
    <path d="M185,80 L185,40 L215,30 L245,45 L275,25 L305,38 L345,20 L345,80 Z" fill="var(--olive)"/>
    <path d="M185,80 L185,55 L215,50 L245,62 L275,48 L305,58 L345,45 L345,80 Z" fill="var(--slate)"/>
    <path d="M185,80 L185,68 L215,66 L245,72 L275,64 L305,70 L345,62 L345,80 Z" fill="var(--purple)"/>
    <rect x="0" y="95" width="350" height="7" fill="var(--slate)"/><text x="3" y="100.5" font-size="4.5" fill="#fff">Year on year comparison</text>
    <g>
      <rect x="30" y="110" width="90" height="5" fill="var(--brown)"/><rect x="30" y="116" width="60" height="5" fill="var(--sage)"/>
      <rect x="30" y="126" width="110" height="5" fill="var(--brown)"/><rect x="30" y="132" width="80" height="5" fill="var(--sage)"/>
      <rect x="30" y="142" width="70" height="5" fill="var(--brown)"/><rect x="30" y="148" width="100" height="5" fill="var(--sage)"/>
      <rect x="30" y="158" width="120" height="5" fill="var(--brown)"/><rect x="30" y="164" width="50" height="5" fill="var(--sage)"/>
      <rect x="30" y="174" width="85" height="5" fill="var(--brown)"/><rect x="30" y="180" width="65" height="5" fill="var(--sage)"/>
    </g>
    <g>
      <rect x="210" y="110" width="60" height="5" fill="var(--brown)"/><rect x="210" y="116" width="95" height="5" fill="var(--sage)"/>
      <rect x="210" y="126" width="80" height="5" fill="var(--brown)"/><rect x="210" y="132" width="40" height="5" fill="var(--sage)"/>
      <rect x="210" y="142" width="110" height="5" fill="var(--brown)"/><rect x="210" y="148" width="70" height="5" fill="var(--sage)"/>
      <rect x="210" y="158" width="50" height="5" fill="var(--brown)"/><rect x="210" y="164" width="90" height="5" fill="var(--sage)"/>
      <rect x="210" y="174" width="100" height="5" fill="var(--brown)"/><rect x="210" y="180" width="75" height="5" fill="var(--sage)"/>
    </g>
  </svg>
  <div class="brand-mini"><i></i>Corvane</div>
</section>

<!-- 2 Flow diagrams -->
<section class="slide">
  <div class="slide-no">7</div>
  <h2 class="slide-title">2 Flow diagrams</h2>
  <div class="slide-sub">Two column layout with bullet text</div>
  <svg class="content" viewBox="0 0 350 195">
    <g>
      <rect x="0" y="0" width="170" height="8" fill="var(--slate)"/><text x="3" y="6" font-size="4.8" fill="#fff">Asset distribution: 2016 (existing structure)</text>
      <rect x="0" y="10" width="170" height="72" fill="var(--pale)"/>
      <rect x="40" y="16" width="90" height="10" fill="var(--sage)"/><text x="68" y="23" font-size="4.5" fill="#fff">Holding company</text>
      <line x1="85" y1="26" x2="85" y2="40" stroke="var(--muted)"/>
      <rect x="20" y="40" width="60" height="10" fill="var(--olive)"/><rect x="90" y="40" width="60" height="10" fill="var(--olive)"/>
      <text x="34" y="47" font-size="4.5" fill="#fff">Operating Co 1</text><text x="104" y="47" font-size="4.5" fill="#fff">Operating Co 2</text>
      <rect x="55" y="62" width="60" height="10" fill="var(--slate-dark)"/><text x="70" y="69" font-size="4.5" fill="#fff">Asset pool</text>
      <line x1="50" y1="50" x2="85" y2="62" stroke="var(--muted)"/><line x1="120" y1="50" x2="85" y2="62" stroke="var(--muted)"/>
    </g>
    <g>
      <rect x="180" y="0" width="170" height="8" fill="var(--slate)"/><text x="183" y="6" font-size="4.8" fill="#fff">Asset distribution: 2018 (new structure)</text>
      <rect x="180" y="10" width="170" height="72" fill="var(--pale)"/>
      <rect x="220" y="16" width="90" height="10" fill="var(--sage)"/><text x="248" y="23" font-size="4.5" fill="#fff">Holding company</text>
      <line x1="265" y1="26" x2="265" y2="40" stroke="var(--muted)"/>
      <rect x="235" y="40" width="60" height="10" fill="var(--olive)"/><text x="250" y="47" font-size="4.5" fill="#fff">Merged entity</text>
      <line x1="265" y1="50" x2="265" y2="62" stroke="var(--muted)"/>
      <rect x="235" y="62" width="60" height="10" fill="var(--slate-dark)"/><text x="250" y="69" font-size="4.5" fill="#fff">Asset pool</text>
    </g>
    <g font-size="4.8">
      <text x="0" y="96" font-weight="600">Key features</text>
      <text x="0" y="105">• Stage held investments (50 %) of target group, in exchange</text><text x="0" y="112">   for shares in stage and further contributions</text>
      <text x="0" y="119">• "Overall" management responsibility for target group</text><text x="0" y="126">• Stage listed on two representatives on the board</text>
      <text x="0" y="133">• Stage holds no responsibility for the new ideas</text>
      <text x="0" y="143" font-weight="600">Considerations</text>
      <text x="0" y="152">• No assessment of costs related with arrangements</text><text x="0" y="159">• Debt to equity ratio confirmed by lenders</text>
      <text x="180" y="96" font-weight="600">Key features</text>
      <text x="180" y="105">• "Overall" management responsibility for target group</text><text x="180" y="112">   sitting in the new structure</text>
      <text x="180" y="119">• Stage holds no further representation at board level</text>
      <text x="180" y="129" font-weight="600">Considerations</text>
      <text x="180" y="138">• Need to set out how to ensure a substantial</text><text x="180" y="145">   dissemination of the holding structure</text>
      <text x="180" y="152">• Ability to provide adequate support levels and</text><text x="180" y="159">   keep all management aligned</text>
    </g>
  </svg>
  <div class="brand-mini"><i></i>Corvane</div>
</section>

<!-- Divider -->
<section class="slide divider">
  <div class="brand"><i></i>Corvane Partners</div>
  <div class="divider-title">Divider page title here</div>
</section>

<!-- 4 Team structures -->
<section class="slide">
  <div class="slide-no">9</div>
  <h2 class="slide-title">4 Team structures</h2>
  <div class="slide-sub">Standard width layout with detailed diagram text</div>
  <svg class="content" viewBox="0 0 350 195">
    <rect x="0" y="0" width="350" height="190" fill="var(--pale)"/>
    <rect x="100" y="6" width="150" height="8" fill="var(--slate)"/><text x="104" y="12" font-size="4.5" fill="#fff">Partners &amp; transaction lead</text>
    <g font-size="4.5">
      <text x="20" y="22">Coordination</text><rect x="100" y="16" width="150" height="14" fill="#fff"/><text x="104" y="22">• Team coordination</text><text x="104" y="28">• Investor relations</text>
      <text x="20" y="40">Key advisor</text><rect x="100" y="33" width="150" height="14" fill="#fff"/><text x="104" y="39">• Deal structuring</text><text x="104" y="45">• Financing terms</text>
    </g>
    <rect x="60" y="54" width="230" height="8" fill="var(--slate-dark)"/><text x="130" y="60" font-size="4.5" fill="#fff">Due diligence advisory team</text>
    <g font-size="4.5">
      <rect x="10" y="68" width="60" height="8" fill="var(--slate)"/><text x="30" y="74" fill="#fff">Legal</text>
      <rect x="78" y="68" width="60" height="8" fill="var(--slate)"/><text x="96" y="74" fill="#fff">Markets</text>
      <rect x="146" y="68" width="60" height="8" fill="var(--slate)"/><text x="162" y="74" fill="#fff">Valuation</text>
      <rect x="214" y="68" width="60" height="8" fill="var(--slate)"/><text x="228" y="74" fill="#fff">Accounting</text>
      <rect x="282" y="68" width="60" height="8" fill="var(--slate)"/><text x="306" y="74" fill="#fff">Tax</text>
      <rect x="10" y="78" width="60" height="95" fill="#fff"/><rect x="78" y="78" width="60" height="95" fill="#fff"/><rect x="146" y="78" width="60" height="95" fill="#fff"/><rect x="214" y="78" width="60" height="95" fill="#fff"/><rect x="282" y="78" width="60" height="95" fill="#fff"/>
      <text x="13" y="86">• Contract review</text><text x="13" y="93">• Corporate records</text><text x="13" y="100">• Litigation check</text><text x="13" y="107">• Permits</text>
      <text x="81" y="86">• Sector data</text><text x="81" y="93">• Peer review</text><text x="81" y="100">• Customer calls</text>
      <text x="149" y="86">• DCF model</text><text x="149" y="93">• Multiples</text><text x="149" y="100">• Sensitivities</text><text x="149" y="107">• Scenarios</text>
      <text x="217" y="86">• Quality of earnings</text><text x="217" y="93">• Working capital</text><text x="217" y="100">• Net debt</text>
      <text x="285" y="86">• Structuring</text><text x="285" y="93">• Tax exposure</text><text x="285" y="100">• Transfer pricing</text>
    </g>
  </svg>
  <div class="strapline">Weekly review: Deal Review Group meets 8:00am each day.</div>
  <div class="brand-mini"><i></i>Corvane</div>
</section>

<!-- 17 Circles, pyramids -->
<section class="slide">
  <div class="slide-no">10</div>
  <h2 class="slide-title">17 Circles, pyramids and other elements</h2>
  <div class="slide-sub">Your subtitle goes here</div>
  <svg class="content" viewBox="0 0 350 195">
    <rect x="0" y="0" width="165" height="8" fill="var(--slate)"/><text x="3" y="6" font-size="4.8" fill="#fff">Your heading here</text>
    <rect x="185" y="0" width="165" height="8" fill="var(--slate)"/><text x="188" y="6" font-size="4.8" fill="#fff">Your heading here</text>
    <path d="M5,30 L130,20 L130,12 L162,35 L130,58 L130,50 L5,40 Z" fill="var(--olive)"/>
    <circle cx="30" cy="35" r="4" fill="#fff"/><circle cx="60" cy="35" r="4" fill="#fff"/><circle cx="90" cy="35" r="4" fill="#fff"/>
    <text x="22" y="48" font-size="4">Text</text><text x="52" y="48" font-size="4">Text</text><text x="82" y="48" font-size="4">Text</text>
    <circle cx="267" cy="50" r="36" fill="none" stroke="var(--rule)" stroke-width="3"/>
    <rect x="238" y="22" width="27" height="27" rx="4" fill="var(--purple)"/><rect x="269" y="22" width="27" height="27" rx="4" fill="var(--slate)"/>
    <rect x="238" y="53" width="27" height="27" rx="4" fill="var(--olive)"/><rect x="269" y="53" width="27" height="27" rx="4" fill="var(--sage)"/>
    <text x="246" y="38" font-size="5" fill="#fff">Text</text><text x="277" y="38" font-size="5" fill="#fff">Text</text><text x="246" y="69" font-size="5" fill="#fff">Text</text><text x="277" y="69" font-size="5" fill="#fff">Text</text>
    <rect x="0" y="98" width="165" height="8" fill="var(--slate)"/><text x="3" y="104" font-size="4.8" fill="#fff">Your heading here</text>
    <rect x="185" y="98" width="165" height="8" fill="var(--slate)"/><text x="188" y="104" font-size="4.8" fill="#fff">Your heading here</text>
    <path d="M82,115 L100,137 L64,137 Z" fill="var(--slate)"/>
    <path d="M62,140 L102,140 L122,163 L42,163 Z" fill="var(--purple)"/>
    <path d="M40,166 L124,166 L140,186 L24,186 Z" fill="var(--brown)"/>
    <text x="76" y="155" font-size="5" fill="#fff">Text</text><text x="76" y="179" font-size="5" fill="#fff">Text</text>
    <g transform="translate(267,150) rotate(45)">
      <rect x="-28" y="-28" width="26" height="26" fill="var(--purple)"/><rect x="2" y="-28" width="26" height="26" fill="var(--olive)"/>
      <rect x="-28" y="2" width="26" height="26" fill="var(--slate)"/><rect x="2" y="2" width="26" height="26" fill="var(--sage)"/>
    </g>
    <text x="243" y="129" font-size="5">Text</text><text x="284" y="152" font-size="5" fill="#fff">Text</text><text x="244" y="152" font-size="5" fill="#fff">Text</text><text x="262" y="176" font-size="5" fill="#fff">Text</text>
  </svg>
  <div class="brand-mini"><i></i>Corvane</div>
</section>

<!-- 33 CVs -->
<section class="slide">
  <div class="slide-no">11</div>
  <h2 class="slide-title">33 CVs</h2>
  <div class="slide-sub">CV details with 4 a page</div>
  <svg class="content" viewBox="0 0 350 195">
    <g font-size="4.5">
      <g>
        <rect x="0" y="0" width="110" height="14" fill="var(--light)"/><text x="3" y="6">Name, surname</text><text x="3" y="12" fill="var(--muted)">Director</text>
        <text x="3" y="24">Global head of healthcare</text><text x="3" y="31">Relevant experience</text><text x="6" y="38">• Transaction 1</text><text x="6" y="45">• Transaction 2</text><text x="6" y="52">• Transaction 3</text>
      </g>
      <g transform="translate(120,0)">
        <rect x="0" y="0" width="110" height="14" fill="var(--light)"/><text x="3" y="6">Name, surname</text><text x="3" y="12" fill="var(--muted)">Director</text>
        <text x="3" y="24">Global head of healthcare</text><text x="3" y="31">Relevant experience</text><text x="6" y="38">• Transaction 1</text><text x="6" y="45">• Transaction 2</text><text x="6" y="52">• Transaction 3</text>
      </g>
      <g transform="translate(0,95)">
        <rect x="0" y="0" width="110" height="14" fill="var(--light)"/><text x="3" y="6">Name, surname</text><text x="3" y="12" fill="var(--muted)">Director</text>
        <text x="3" y="24">Global head of healthcare</text><text x="3" y="31">Relevant experience</text><text x="6" y="38">• Transaction 1</text><text x="6" y="45">• Transaction 2</text><text x="6" y="52">• Transaction 3</text>
      </g>
      <g transform="translate(120,95)">
        <rect x="0" y="0" width="110" height="14" fill="var(--light)"/><text x="3" y="6">Name, surname</text><text x="3" y="12" fill="var(--muted)">Director</text>
        <text x="3" y="24">Global head of healthcare</text><text x="3" y="31">Relevant experience</text><text x="6" y="38">• Transaction 1</text><text x="6" y="45">• Transaction 2</text><text x="6" y="52">• Transaction 3</text>
      </g>
    </g>
  </svg>
  <div class="brand-mini"><i></i>Corvane</div>
</section>

<!-- 34 CVs -->
<section class="slide">
  <div class="slide-no">12</div>
  <h2 class="slide-title">34 CVs</h2>
  <div class="slide-sub">CV details with 6 a page</div>
  <svg class="content" viewBox="0 0 350 195">
    <g font-size="4.5">
      <g><rect width="108" height="14" fill="var(--light)"/><text x="3" y="6">Name, surname</text><text x="3" y="12" fill="var(--muted)">Director</text><text x="3" y="24">Global head of healthcare</text><text x="3" y="31">Relevant experience</text><text x="6" y="38">• Transaction 1</text><text x="6" y="45">• Transaction 2</text><text x="6" y="52">• Transaction 3</text></g>
      <g transform="translate(121,0)"><rect width="108" height="14" fill="var(--light)"/><text x="3" y="6">Name, surname</text><text x="3" y="12" fill="var(--muted)">Director</text><text x="3" y="24">Global head of healthcare</text><text x="3" y="31">Relevant experience</text><text x="6" y="38">• Transaction 1</text><text x="6" y="45">• Transaction 2</text><text x="6" y="52">• Transaction 3</text></g>
      <g transform="translate(242,0)"><rect width="108" height="14" fill="var(--light)"/><text x="3" y="6">Name, surname</text><text x="3" y="12" fill="var(--muted)">Director</text><text x="3" y="24">Global head of healthcare</text><text x="3" y="31">Relevant experience</text><text x="6" y="38">• Transaction 1</text><text x="6" y="45">• Transaction 2</text><text x="6" y="52">• Transaction 3</text></g>
      <g transform="translate(0,95)"><rect width="108" height="14" fill="var(--light)"/><text x="3" y="6">Name, surname</text><text x="3" y="12" fill="var(--muted)">Director</text><text x="3" y="24">Global head of healthcare</text><text x="3" y="31">Relevant experience</text><text x="6" y="38">• Transaction 1</text><text x="6" y="45">• Transaction 2</text><text x="6" y="52">• Transaction 3</text></g>
      <g transform="translate(121,95)"><rect width="108" height="14" fill="var(--light)"/><text x="3" y="6">Name, surname</text><text x="3" y="12" fill="var(--muted)">Director</text><text x="3" y="24">Global head of healthcare</text><text x="3" y="31">Relevant experience</text><text x="6" y="38">• Transaction 1</text><text x="6" y="45">• Transaction 2</text><text x="6" y="52">• Transaction 3</text></g>
      <g transform="translate(242,95)"><rect width="108" height="14" fill="var(--light)"/><text x="3" y="6">Name, surname</text><text x="3" y="12" fill="var(--muted)">Director</text><text x="3" y="24">Global head of healthcare</text><text x="3" y="31">Relevant experience</text><text x="6" y="38">• Transaction 1</text><text x="6" y="45">• Transaction 2</text><text x="6" y="52">• Transaction 3</text></g>
    </g>
  </svg>
  <div class="brand-mini"><i></i>Corvane</div>
</section>

<!-- 35 Quotes -->
<section class="slide">
  <div class="slide-no">13</div>
  <h2 class="slide-title">35 Quotes</h2>
  <div class="slide-sub">Two column layout</div>
  <svg class="content" viewBox="0 0 350 195">
    <rect x="0" y="0" width="165" height="8" fill="var(--slate)"/><text x="3" y="6" font-size="4.8" fill="#fff">Companies: 2017 outlook by year</text>
    <g stroke="var(--light)"><line x1="15" y1="25" x2="160" y2="25"/><line x1="15" y1="45" x2="160" y2="45"/><line x1="15" y1="65" x2="160" y2="65"/><line x1="15" y1="85" x2="160" y2="85"/></g>
    <polyline points="20,70 50,62 80,64 110,58 140,60 158,56" fill="none" stroke="var(--purple)"/>
    <polyline points="20,78 50,75 80,72 110,74 140,70 158,71" fill="none" stroke="var(--olive)"/>
    <text x="0" y="100" font-size="4.5" fill="var(--muted)">Source: data 2017</text>
    <text x="0" y="112" font-size="5">Region 2016</text><text x="90" y="112" font-size="5">Volume 2016</text>
    <g transform="translate(35,145)"><circle r="26" fill="var(--slate)"/><path d="M0,0 L0,-26 A26,26 0 0,1 24,10 Z" fill="var(--purple)"/><path d="M0,0 L24,10 A26,26 0 0,1 -6,25 Z" fill="var(--olive)"/></g>
    <g transform="translate(125,145)"><circle r="26" fill="var(--sage)"/><path d="M0,0 L0,-26 A26,26 0 0,1 26,0 Z" fill="var(--slate)"/><path d="M0,0 L26,0 A26,26 0 0,1 -10,24 Z" fill="var(--purple)"/></g>
    <rect x="180" y="0" width="170" height="8" fill="var(--slate)"/><text x="183" y="6" font-size="4.8" fill="#fff">Key observations</text>
    <rect x="180" y="10" width="170" height="160" fill="var(--pale)"/>
    <g font-size="4.6">
      <text x="186" y="22">"Investors are increasingly selective about sectors and</text><text x="186" y="29">favour businesses with a clear path to recovery. The</text><text x="186" y="36">turnaround cycle has shortened and owners are more</text><text x="186" y="43">willing to consider partners with operating experience."</text>
      <text x="186" y="52" fill="var(--muted)">– Senior Partner, Corvane Partners</text>
      <text x="186" y="70">"Lenders remain focused on cash generation and the</text><text x="186" y="77">strength of management teams rather than asset value</text><text x="186" y="84">alone when assessing restructuring proposals."</text>
      <text x="186" y="93" fill="var(--muted)">– Managing Director, regional bank</text>
      <text x="186" y="111">"The best outcomes come where founders stay involved</text><text x="186" y="118">through the transition period."</text>
      <text x="186" y="127" fill="var(--muted)">– Company founder</text>
    </g>
  </svg>
  <div class="strapline">A strapline may be placed here</div>
  <div class="brand-mini"><i></i>Corvane</div>
</section>

<!-- 36 Timetables -->
<section class="slide">
  <div class="slide-no">14</div>
  <h2 class="slide-title">36 Timetables</h2>
  <div class="slide-sub">Key dates timetable</div>
  <svg class="content" viewBox="0 0 350 195">
    <text x="0" y="45" font-size="5">Events</text><text x="0" y="140" font-size="5">Milestones</text>
    <rect x="30" y="82" width="320" height="8" fill="var(--slate)"/>
    <rect x="30" y="90" width="320" height="7" fill="var(--light)"/>
    <g font-size="4" fill="#fff"><text x="34" y="88">2016</text><text x="200" y="88">2017</text></g>
    <g stroke="var(--muted)" stroke-width=".6">
      <line x1="60" y1="20" x2="60" y2="82"/><line x1="90" y1="35" x2="90" y2="82"/><line x1="120" y1="15" x2="120" y2="82"/><line x1="150" y1="40" x2="150" y2="82"/><line x1="210" y1="25" x2="210" y2="82"/><line x1="260" y1="30" x2="260" y2="82"/><line x1="300" y1="20" x2="300" y2="82"/>
      <line x1="70" y1="97" x2="70" y2="130"/><line x1="110" y1="97" x2="110" y2="125"/><line x1="180" y1="97" x2="180" y2="140"/><line x1="240" y1="97" x2="240" y2="120"/><line x1="320" y1="97" x2="320" y2="130"/>
    </g>
    <g font-size="4">
      <text x="62" y="22">Launch</text><text x="92" y="37">Review</text><text x="122" y="17">Mandate</text><text x="152" y="42">Data room</text><text x="212" y="27">Bids due</text><text x="262" y="32">Signing</text><text x="302" y="22">Closing</text>
      <text x="72" y="135">• Kick-off</text><text x="72" y="141">• Teaser sent</text>
      <text x="112" y="130">• NDA signed</text><text x="112" y="136">• IM released</text>
      <text x="182" y="145">• Site visits</text><text x="182" y="151">• Q&amp;A</text>
      <text x="242" y="125">• Final offers</text><text x="242" y="131">• SPA drafting</text>
      <text x="300" y="135">• Completion</text>
    </g>
  </svg>
  <div class="brand-mini"><i></i>Corvane</div>
</section>

<!-- 37 Timetables -->
<section class="slide">
  <div class="slide-no">15</div>
  <h2 class="slide-title">37 Timetables</h2>
  <div class="slide-sub">Transaction process timetable with side headings</div>
  <svg class="content" viewBox="0 0 350 195">
    <text x="0" y="6" font-size="4.5">Month</text><text x="0" y="13" font-size="4.5">Week</text>
    <rect x="45" y="0" width="305" height="14" fill="var(--slate)"/>
    <g font-size="4" fill="#fff"><text x="60" y="6">January</text><text x="140" y="6">February</text><text x="220" y="6">March</text><text x="300" y="6">April</text></g>
    <g font-size="4.8"><text x="0" y="35">Corporate finance</text><text x="0" y="90">Public capital</text><text x="0" y="97">markets</text><text x="0" y="150">Research, sales</text><text x="0" y="157">&amp; trading</text></g>
    <g stroke="var(--light)"><line x1="0" y1="65" x2="350" y2="65"/><line x1="0" y1="125" x2="350" y2="125"/></g>
    <g fill="var(--light)">
      <rect x="50" y="20" width="60" height="6"/><rect x="70" y="30" width="110" height="6"/><rect x="110" y="40" width="80" height="6"/><rect x="160" y="50" width="150" height="6"/>
      <rect x="60" y="75" width="130" height="6"/><rect x="120" y="85" width="100" height="6"/><rect x="170" y="95" width="90" height="6"/><rect x="200" y="105" width="120" height="6"/>
      <rect x="80" y="135" width="70" height="6"/><rect x="190" y="145" width="90" height="6"/><rect x="260" y="160" width="70" height="6"/><rect x="300" y="172" width="45" height="6"/>
    </g>
  </svg>
  <div class="brand-mini"><i></i>Corvane</div>
</section>

<!-- 39 Timetables -->
<section class="slide">
  <div class="slide-no">16</div>
  <h2 class="slide-title">39 Timetables</h2>
  <div class="slide-sub">Indicative timetable with detailed row titles and numbering</div>
  <svg class="content" viewBox="0 0 350 195">
    <rect x="0" y="0" width="350" height="6" fill="var(--slate)"/>
    <g font-size="4" fill="#fff"><text x="140" y="5">1</text><text x="175" y="5">2</text><text x="210" y="5">3</text><text x="245" y="5">4</text><text x="280" y="5">5</text><text x="315" y="5">6</text></g>
    <rect x="0" y="7" width="350" height="5" fill="var(--light)"/>
    <g font-size="3.8">
      <text x="2" y="19" font-weight="600">A  Preparation phase</text>
      <text x="6" y="26">• Preparation of information memorandum</text><text x="6" y="32">• Preparation of financial model</text><text x="6" y="38">• Preparation of vendor due diligence</text><text x="6" y="44">• Preparation of management presentation</text><text x="6" y="50">• Marketing approach</text>
      <text x="2" y="58" font-weight="600">B  Phase I – Indicative offers</text>
      <text x="6" y="65">• Distribution of teaser</text><text x="6" y="71">• Signing of confidentiality agreements</text><text x="6" y="77">• Distribution of memorandum</text><text x="6" y="83">• Receipt of indicative offers</text><text x="6" y="89">• Selection of shortlist</text>
      <text x="2" y="97" font-weight="600">C  Phase II – Binding offers</text>
      <text x="6" y="104">• Access to data room</text><text x="6" y="110">• Management presentations</text><text x="6" y="116">• Site visits</text><text x="6" y="122">• Draft SPA distributed</text><text x="6" y="128">• Receipt of binding offers</text><text x="6" y="134">• Negotiation</text><text x="6" y="140">• Signing</text>
    </g>
    <g fill="var(--light)" stroke="var(--muted)" stroke-width=".3">
      <rect x="130" y="22" width="40" height="4"/><rect x="135" y="28" width="50" height="4"/><rect x="140" y="34" width="35" height="4"/><rect x="150" y="40" width="45" height="4"/><rect x="160" y="46" width="30" height="4"/>
      <rect x="185" y="61" width="20" height="4"/><rect x="190" y="67" width="35" height="4"/><rect x="200" y="73" width="30" height="4"/><rect x="215" y="79" width="25" height="4"/><rect x="230" y="85" width="15" height="4"/>
      <rect x="240" y="100" width="50" height="4"/><rect x="250" y="106" width="30" height="4"/><rect x="255" y="112" width="25" height="4"/><rect x="270" y="118" width="30" height="4"/><rect x="290" y="124" width="20" height="4"/><rect x="300" y="130" width="30" height="4"/><rect x="325" y="136" width="15" height="4"/>
    </g>
  </svg>
  <div class="brand-mini"><i></i>Corvane</div>
</section>

<!-- 40 Timetable -->
<section class="slide">
  <div class="slide-no">17</div>
  <h2 class="slide-title">40 Timetable</h2>
  <div class="slide-sub">Your subtitle goes here</div>
  <svg class="content" viewBox="0 0 350 195">
    <rect x="0" y="0" width="350" height="8" fill="var(--slate)"/>
    <g font-size="4" fill="#fff"><text x="80" y="6">1</text><text x="130" y="6">2</text><text x="180" y="6">3</text><text x="230" y="6">4</text><text x="280" y="6">5</text><text x="330" y="6">6</text></g>
    <g>
      <rect x="0" y="14" width="8" height="10" fill="var(--slate)"/><rect x="10" y="14" width="55" height="10" fill="var(--purple)"/>
      <rect x="0" y="30" width="8" height="10" fill="var(--slate)"/><rect x="10" y="30" width="55" height="10" fill="var(--purple)"/>
      <rect x="0" y="46" width="8" height="10" fill="var(--slate)"/><rect x="10" y="46" width="55" height="10" fill="var(--purple)"/>
      <rect x="0" y="62" width="8" height="10" fill="var(--slate)"/><rect x="10" y="62" width="55" height="10" fill="var(--purple)"/>
      <rect x="0" y="78" width="8" height="10" fill="var(--slate)"/><rect x="10" y="78" width="55" height="10" fill="var(--purple)"/>
      <rect x="0" y="94" width="8" height="10" fill="var(--slate)"/><rect x="10" y="94" width="55" height="10" fill="var(--purple)"/>
      <rect x="0" y="110" width="8" height="10" fill="var(--slate)"/><rect x="10" y="110" width="55" height="10" fill="var(--purple)"/>
      <rect x="0" y="126" width="8" height="10" fill="var(--slate)"/><rect x="10" y="126" width="55" height="10" fill="var(--purple)"/>
      <rect x="0" y="142" width="8" height="10" fill="var(--slate)"/><rect x="10" y="142" width="55" height="10" fill="var(--purple)"/>
      <rect x="0" y="158" width="8" height="10" fill="var(--slate)"/><rect x="10" y="158" width="55" height="10" fill="var(--purple)"/>
    </g>
    <g fill="var(--light)">
      <rect x="70" y="16" width="60" height="6"/><rect x="90" y="32" width="70" height="6"/><rect x="110" y="48" width="80" height="6"/><rect x="130" y="64" width="50" height="6"/><rect x="150" y="80" width="70" height="6"/>
      <rect x="170" y="96" width="100" height="6"/><rect x="190" y="112" width="70" height="6"/><rect x="210" y="128" width="90" height="6"/><rect x="230" y="144" width="80" height="6"/><rect x="260" y="160" width="85" height="6"/>
    </g>
    <path d="M300,100 L306,106 L300,112 L294,106 Z" fill="var(--olive)"/>
    <path d="M333,155 L340,163 L333,171 L326,163 Z" fill="var(--sage)"/>
  </svg>
  <div class="brand-mini"><i></i>Corvane</div>
</section>

<!-- 41 Timetable -->
<section class="slide">
  <div class="slide-no">18</div>
  <h2 class="slide-title sentence">41 Timetable</h2>
  <div class="slide-sub">Your subtitle goes here</div>
  <svg class="content" viewBox="0 0 350 195">
    <rect x="0" y="0" width="350" height="8" fill="var(--slate)"/><text x="3" y="6" font-size="4.8" fill="#fff">Timeline</text>
    <rect x="0" y="10" width="350" height="150" fill="var(--pale)"/>
    <line x1="5" y1="85" x2="345" y2="85" stroke="var(--muted)" stroke-width=".6"/>
    <g fill="var(--light)" stroke="var(--muted)" stroke-width=".3">
      <rect x="8" y="79" width="20" height="12"/><rect x="34" y="79" width="20" height="12"/><rect x="60" y="79" width="20" height="12"/><rect x="86" y="79" width="20" height="12"/><rect x="112" y="79" width="20" height="12"/><rect x="138" y="79" width="20" height="12"/><rect x="164" y="79" width="20" height="12"/><rect x="216" y="79" width="20" height="12"/><rect x="242" y="79" width="20" height="12"/><rect x="268" y="79" width="20" height="12"/><rect x="294" y="79" width="20" height="12"/><rect x="320" y="79" width="20" height="12"/>
    </g>
    <rect x="190" y="79" width="20" height="12" fill="var(--brown)"/>
    <g font-size="3.8"><text x="12" y="87">Jan</text><text x="38" y="87">Feb</text><text x="64" y="87">Mar</text><text x="90" y="87">Apr</text><text x="115" y="87">May</text><text x="142" y="87">Jun</text><text x="168" y="87">Jul</text><text x="194" y="87" fill="#fff">Aug</text><text x="219" y="87">Sep</text><text x="246" y="87">Oct</text><text x="271" y="87">Nov</text><text x="297" y="87">Dec</text><text x="323" y="87">Jan</text></g>
    <line x1="200" y1="30" x2="200" y2="79" stroke="var(--muted)" stroke-width=".5"/>
    <text x="203" y="34" font-size="4">Key milestone</text>
    <line x1="96" y1="91" x2="96" y2="130" stroke="var(--muted)" stroke-width=".5"/><text x="99" y="128" font-size="4">Review point</text>
  </svg>
  <div class="brand-mini"><i></i>Corvane</div>
</section>

<!-- 46 SWOT -->
<section class="slide">
  <div class="slide-no">19</div>
  <h2 class="slide-title">46 SWOT analysis</h2>
  <div class="slide-sub">Your subtitle goes here</div>
  <svg class="content" viewBox="0 0 350 195">
    <rect x="0" y="0" width="350" height="8" fill="var(--brown)"/><text x="3" y="6" font-size="4.8" fill="#fff">Strengths</text><text x="318" y="6" font-size="4.8" fill="#fff">Weaknesses</text>
    <rect x="0" y="8" width="350" height="172" fill="none" stroke="var(--rule)"/>
    <line x1="175" y1="8" x2="175" y2="172" stroke="var(--rule)"/><line x1="0" y1="90" x2="350" y2="90" stroke="var(--rule)"/>
    <g font-size="4.6">
      <text x="6" y="18">Text</text><text x="8" y="25">• Bullet text</text><text x="14" y="32">– Sub bullet</text><text x="20" y="39">· Sub-sub bullet</text>
      <text x="181" y="18">Text</text><text x="183" y="25">• Bullet text</text><text x="189" y="32">– Sub bullet</text>
      <text x="6" y="100">Text</text><text x="8" y="107">• Bullet text</text><text x="14" y="114">– Sub bullet</text>
      <text x="181" y="100">Text</text><text x="183" y="107">• Bullet text</text><text x="189" y="114">– Sub bullet</text><text x="195" y="121">· Sub-sub bullet</text>
    </g>
    <rect x="0" y="172" width="350" height="8" fill="var(--slate)"/><text x="3" y="178" font-size="4.8" fill="#fff">Opportunities</text><text x="330" y="178" font-size="4.8" fill="#fff">Threats</text>
  </svg>
  <div class="strapline">A strapline may be placed here</div>
  <div class="brand-mini"><i></i>Corvane</div>
</section>

<!-- 47 SWOT -->
<section class="slide">
  <div class="slide-no">20</div>
  <h2 class="slide-title sentence">47 SWOT analysis</h2>
  <div class="slide-sub">Your subtitle goes here</div>
  <svg class="content" viewBox="0 0 350 195">
    <rect x="30" y="0" width="290" height="8" fill="var(--slate)"/><text x="33" y="6" font-size="4.8" fill="#fff">SWOT analysis</text>
    <rect x="30" y="8" width="290" height="170" fill="none" stroke="var(--rule)"/>
    <line x1="175" y1="8" x2="175" y2="178" stroke="var(--rule)"/><line x1="30" y1="93" x2="320" y2="93" stroke="var(--rule)"/>
    <g font-size="4.6">
      <text x="36" y="18">Text</text><text x="38" y="25">• Bullet text</text><text x="44" y="32">– Sub bullet</text><text x="50" y="39">· Sub-sub bullet</text>
      <text x="181" y="18">Text</text><text x="183" y="25">• Bullet text</text><text x="189" y="32">– Sub bullet</text>
      <text x="36" y="130">Text</text><text x="38" y="137">• Bullet text</text><text x="44" y="144">– Sub bullet</text>
      <text x="200" y="130">Text</text><text x="202" y="137">• Bullet text</text><text x="208" y="144">– Sub bullet</text>
    </g>
    <path d="M175,63 L205,93 L175,93 Z" fill="var(--purple)"/>
    <path d="M175,63 L145,93 L175,93 Z" fill="var(--slate)"/>
    <path d="M145,93 L175,123 L175,93 Z" fill="var(--olive)"/>
    <path d="M205,93 L175,123 L175,93 Z" fill="var(--sage)"/>
    <g font-size="5" fill="#fff"><text x="161" y="89">S</text><text x="183" y="89">W</text><text x="161" y="103">O</text><text x="183" y="103">T</text></g>
  </svg>
  <div class="brand-mini"><i></i>Corvane</div>
</section>

<!-- 51 Value chain -->
<section class="slide">
  <div class="slide-no">21</div>
  <h2 class="slide-title">51 Value chain</h2>
  <div class="slide-sub">Your subtitle here</div>
  <svg class="content" viewBox="0 0 350 195">
    <g fill="var(--slate)">
      <path d="M0,0 L44,0 L50,5 L44,10 L0,10 Z"/><path d="M50,0 L94,0 L100,5 L94,10 L50,10 L56,5 Z"/><path d="M100,0 L144,0 L150,5 L144,10 L100,10 L106,5 Z"/><path d="M150,0 L194,0 L200,5 L194,10 L150,10 L156,5 Z"/><path d="M200,0 L244,0 L250,5 L244,10 L200,10 L206,5 Z"/><path d="M250,0 L294,0 L300,5 L294,10 L250,10 L256,5 Z"/><path d="M300,0 L350,0 L350,10 L300,10 L306,5 Z"/>
    </g>
    <g fill="var(--pale)"><rect x="0" y="12" width="47" height="160"/><rect x="50" y="12" width="47" height="160"/><rect x="100" y="12" width="47" height="160"/><rect x="150" y="12" width="47" height="160"/><rect x="200" y="12" width="47" height="160"/><rect x="250" y="12" width="47" height="160"/><rect x="300" y="12" width="50" height="160"/></g>
    <g font-size="4.3"><text x="3" y="22">• Sourcing</text><text x="53" y="22">• Inbound</text><text x="103" y="22">• Production</text><text x="153" y="22">• Outbound</text><text x="203" y="22">• Marketing</text><text x="253" y="22">• Sales</text><text x="303" y="22">• Service</text></g>
  </svg>
  <div class="brand-mini"><i></i>Corvane</div>
</section>

<!-- 52 Value chain -->
<section class="slide">
  <div class="slide-no">22</div>
  <h2 class="slide-title sentence">52 Value chain</h2>
  <div class="slide-sub">Your subtitle here</div>
  <svg class="content" viewBox="0 0 350 195">
    <g fill="var(--light)">
      <path d="M0,0 L105,0 L115,8 L105,16 L0,16 Z"/><path d="M118,0 L223,0 L233,8 L223,16 L118,16 L128,8 Z"/><path d="M236,0 L340,0 L350,8 L340,16 L236,16 L246,8 Z"/>
    </g>
    <g font-size="5"><text x="4" y="10">Activity one</text><text x="132" y="10">Activity two</text><text x="250" y="10">Activity three</text></g>
    <g font-size="4.6">
      <text x="4" y="28">• Bullet text</text><text x="10" y="35">– Sub bullet</text><text x="4" y="42">• Bullet text</text><text x="10" y="49">– Sub bullet</text><text x="16" y="56">· Sub-sub bullet</text>
      <text x="122" y="28">• Bullet text</text><text x="128" y="35">– Sub bullet</text><text x="122" y="42">• Bullet text</text><text x="128" y="49">– Sub bullet</text>
      <text x="240" y="28">• Bullet text</text><text x="246" y="35">– Sub bullet</text><text x="240" y="42">• Bullet text</text><text x="246" y="49">– Sub bullet</text><text x="252" y="56">· Sub-sub bullet</text>
    </g>
  </svg>
  <div class="brand-mini"><i></i>Corvane</div>
</section>

<!-- 58 Other diagrams -->
<section class="slide">
  <div class="slide-no">23</div>
  <h2 class="slide-title sentence">58 Other diagrams</h2>
  <div class="slide-sub">Your subtitle here</div>
  <svg class="content" viewBox="0 0 350 195">
    <rect x="0" y="0" width="165" height="8" fill="var(--slate)"/><text x="3" y="6" font-size="4.8" fill="#fff">Puzzle pieces</text>
    <rect x="185" y="0" width="165" height="8" fill="var(--slate)"/><text x="188" y="6" font-size="4.8" fill="#fff">Harvey balls</text>
    <rect x="0" y="10" width="165" height="170" fill="var(--pale)"/><rect x="185" y="10" width="165" height="170" fill="var(--pale)"/>
    <g>
      <rect x="20" y="25" width="35" height="35" fill="var(--purple)"/><rect x="55" y="25" width="35" height="35" fill="var(--slate)"/><rect x="90" y="25" width="35" height="35" fill="var(--purple)"/>
      <rect x="20" y="60" width="35" height="35" fill="var(--slate)"/><rect x="55" y="60" width="35" height="35" fill="var(--purple)"/><rect x="90" y="60" width="35" height="35" fill="var(--slate)"/>
      <rect x="55" y="95" width="50" height="50" fill="var(--brown)"/>
      <circle cx="55" cy="42" r="5" fill="var(--slate)"/><circle cx="90" cy="78" r="5" fill="var(--purple)"/><circle cx="38" cy="60" r="5" fill="var(--purple)"/>
    </g>
    <g>
      <circle cx="205" cy="30" r="8" fill="var(--olive)"/><circle cx="235" cy="30" r="8" fill="var(--slate)"/><circle cx="265" cy="30" r="8" fill="#fff" stroke="var(--rule)"/><path d="M265,30 L265,22 A8,8 0 0,1 273,30 Z" fill="var(--brown)"/>
      <circle cx="205" cy="60" r="8" fill="var(--purple)"/><circle cx="235" cy="60" r="8" fill="#fff" stroke="var(--rule)"/><path d="M235,60 L235,52 A8,8 0 1,1 227,60 Z" fill="var(--olive)"/><circle cx="265" cy="60" r="8" fill="var(--sage)"/>
      <circle cx="205" cy="90" r="8" fill="#fff" stroke="var(--rule)"/><path d="M205,90 L205,82 A8,8 0 0,1 205,98 Z" fill="var(--olive)"/><circle cx="235" cy="90" r="8" fill="var(--olive)"/><circle cx="265" cy="90" r="8" fill="#fff" stroke="var(--rule)"/>
      <circle cx="205" cy="120" r="8" fill="var(--slate)"/><circle cx="235" cy="120" r="8" fill="#fff" stroke="var(--rule)"/><circle cx="265" cy="120" r="8" fill="var(--purple)"/>
      <circle cx="205" cy="150" r="8" fill="#fff" stroke="var(--rule)"/><circle cx="235" cy="150" r="8" fill="var(--sage)"/><circle cx="265" cy="150" r="8" fill="#fff" stroke="var(--rule)"/>
    </g>
  </svg>
  <div class="brand-mini"><i></i>Corvane</div>
</section>

<!-- 67 Brazil -->
<section class="slide">
  <div class="slide-no">24</div>
  <h2 class="slide-title">67 Brazil</h2>
  <div class="slide-sub">Your subtitle here</div>
  <div class="map" role="img" aria-label="Map of Brazil showing state boundaries, light gray"></div>
  <div class="brand-mini"><i></i>Corvane</div>
</section>

<!-- 8 Table -->
<section class="slide">
  <div class="slide-no">25</div>
  <h2 class="slide-title sentence">8 Table</h2>
  <div class="slide-sub">Your subtitle here</div>
  <svg class="content" viewBox="0 0 350 195">
    <rect x="0" y="0" width="350" height="8" fill="var(--slate)"/>
    <g>
      <rect x="0" y="10" width="70" height="26" fill="var(--light)"/><rect x="0" y="38" width="70" height="26" fill="var(--light)"/><rect x="0" y="66" width="70" height="26" fill="var(--light)"/><rect x="0" y="94" width="70" height="26" fill="var(--light)"/><rect x="0" y="122" width="70" height="26" fill="var(--light)"/><rect x="0" y="150" width="70" height="26" fill="var(--light)"/>
    </g>
    <g stroke="var(--rule)"><line x1="70" y1="37" x2="350" y2="37"/><line x1="70" y1="65" x2="350" y2="65"/><line x1="70" y1="93" x2="350" y2="93"/><line x1="70" y1="121" x2="350" y2="121"/><line x1="70" y1="149" x2="350" y2="149"/><line x1="70" y1="177" x2="350" y2="177"/></g>
    <g font-size="4.6"><text x="78" y="20">• Bullet text</text><text x="78" y="48">• Bullet text</text><text x="78" y="76">• Bullet text</text><text x="78" y="104">• Bullet text</text><text x="78" y="132">• Bullet text</text><text x="78" y="160">• Bullet text</text></g>
  </svg>
  <div class="strapline">A strapline may be placed here</div>
  <div class="brand-mini"><i></i>Corvane</div>
</section>

<!-- 10 Table -->
<section class="slide">
  <div class="slide-no">26</div>
  <h2 class="slide-title">10 Table</h2>
  <div class="slide-sub">Your subtitle here</div>
  <svg class="content" viewBox="0 0 350 195">
    <rect x="0" y="0" width="240" height="8" fill="var(--slate)"/><rect x="265" y="0" width="85" height="8" fill="var(--slate)"/>
    <rect x="0" y="10" width="240" height="175" fill="var(--light)"/>
    <rect x="265" y="10" width="85" height="175" fill="var(--sage-light)"/>
    <g stroke="#fff"><line x1="0" y1="45" x2="240" y2="45"/><line x1="0" y1="80" x2="240" y2="80"/><line x1="0" y1="115" x2="240" y2="115"/><line x1="0" y1="150" x2="240" y2="150"/><line x1="265" y1="45" x2="350" y2="45"/><line x1="265" y1="80" x2="350" y2="80"/><line x1="265" y1="115" x2="350" y2="115"/><line x1="265" y1="150" x2="350" y2="150"/></g>
    <g fill="var(--muted)"><path d="M248,23 L256,27 L248,31 Z"/><path d="M248,58 L256,62 L248,66 Z"/><path d="M248,93 L256,97 L248,101 Z"/><path d="M248,128 L256,132 L248,136 Z"/><path d="M248,163 L256,167 L248,171 Z"/></g>
    <g font-size="4.6"><text x="8" y="20">• Bullet text</text><text x="8" y="55">• Bullet text</text><text x="8" y="90">• Bullet text</text><text x="8" y="125">• Bullet text</text><text x="8" y="160">• Bullet text</text></g>
  </svg>
  <div class="brand-mini"><i></i>Corvane</div>
</section>

<!-- 12 Table -->
<section class="slide">
  <div class="slide-no">27</div>
  <h2 class="slide-title">12 Table</h2>
  <div class="slide-sub">Your subtitle here</div>
  <svg class="content" viewBox="0 0 350 195">
    <rect x="0" y="0" width="350" height="8" fill="var(--slate)"/>
    <rect x="120" y="10" width="110" height="150" fill="var(--sage-light)"/>
    <g fill="var(--light)"><rect x="0" y="12" width="110" height="34"/><rect x="0" y="50" width="110" height="34"/><rect x="0" y="88" width="110" height="34"/><rect x="0" y="126" width="110" height="34"/>
    <rect x="240" y="12" width="110" height="34"/><rect x="240" y="50" width="110" height="34"/><rect x="240" y="88" width="110" height="34"/><rect x="240" y="126" width="110" height="34"/></g>
    <g fill="var(--muted)"><path d="M112,25 L118,29 L112,33 Z"/><path d="M232,25 L238,29 L232,33 Z"/><path d="M232,63 L238,67 L232,71 Z"/><path d="M232,101 L238,105 L232,109 Z"/></g>
    <g font-size="4.6"><text x="6" y="22">• Bullet text</text><text x="12" y="29">– Sub bullet</text><text x="126" y="22">• Bullet text</text><text x="132" y="29">– Sub bullet</text><text x="246" y="22">• Bullet text</text><text x="246" y="60">• Bullet text</text></g>
  </svg>
  <div class="brand-mini"><i></i>Corvane</div>
</section>

<!-- 13 Table -->
<section class="slide">
  <div class="slide-no">28</div>
  <h2 class="slide-title">13 Table</h2>
  <div class="slide-sub">Your subtitle here</div>
  <svg class="content" viewBox="0 0 350 195">
    <rect x="0" y="0" width="350" height="8" fill="var(--slate)"/>
    <g>
      <rect x="0" y="10" width="20" height="16" fill="var(--olive)"/><rect x="22" y="10" width="300" height="16" fill="var(--sage-light)"/><rect x="324" y="10" width="26" height="16" fill="var(--olive)"/>
      <rect x="0" y="28" width="20" height="16" fill="var(--olive)"/><rect x="22" y="28" width="300" height="16" fill="var(--sage-light)"/><rect x="324" y="28" width="26" height="16" fill="var(--olive)"/>
      <rect x="0" y="46" width="20" height="16" fill="var(--olive)"/><rect x="22" y="46" width="300" height="16" fill="var(--sage-light)"/><rect x="324" y="46" width="26" height="16" fill="var(--olive)"/>
      <rect x="0" y="64" width="20" height="16" fill="var(--olive)"/><rect x="22" y="64" width="300" height="16" fill="var(--sage-light)"/><rect x="324" y="64" width="26" height="16" fill="var(--olive)"/>
      <rect x="0" y="82" width="20" height="16" fill="var(--olive)"/><rect x="22" y="82" width="300" height="16" fill="var(--sage-light)"/><rect x="324" y="82" width="26" height="16" fill="var(--olive)"/>
      <rect x="0" y="100" width="20" height="16" fill="var(--olive)"/><rect x="22" y="100" width="300" height="16" fill="var(--sage-light)"/><rect x="324" y="100" width="26" height="16" fill="var(--olive)"/>
      <rect x="0" y="118" width="20" height="16" fill="var(--olive)"/><rect x="22" y="118" width="300" height="16" fill="var(--sage-light)"/><rect x="324" y="118" width="26" height="16" fill="var(--olive)"/>
      <rect x="0" y="136" width="20" height="16" fill="var(--olive)"/><rect x="22" y="136" width="300" height="16" fill="var(--sage-light)"/><rect x="324" y="136" width="26" height="16" fill="var(--olive)"/>
      <rect x="0" y="154" width="20" height="16" fill="var(--olive)"/><rect x="22" y="154" width="300" height="16" fill="var(--sage-light)"/><rect x="324" y="154" width="26" height="16" fill="var(--olive)"/>
    </g>
    <g font-size="4.6"><text x="28" y="20">• Bullet text</text><text x="28" y="38">• Bullet text</text><text x="28" y="56">• Bullet text</text><text x="28" y="74">• Bullet text</text><text x="28" y="92">• Bullet text</text><text x="28" y="110">• Bullet text</text><text x="28" y="128">• Bullet text</text><text x="28" y="146">• Bullet text</text><text x="28" y="164">• Bullet text</text></g>
    <g font-size="4.6" fill="#fff"><text x="333" y="20">1.0</text><text x="333" y="38">2.0</text><text x="333" y="56">3.0</text><text x="333" y="74">4.0</text><text x="333" y="92">5.0</text><text x="333" y="110">6.0</text><text x="333" y="128">7.0</text><text x="333" y="146">8.0</text><text x="333" y="164">9.0</text></g>
  </svg>
  <div class="brand-mini"><i></i>Corvane</div>
</section>

<!-- 17 Table -->
<section class="slide">
  <div class="slide-no">29</div>
  <h2 class="slide-title">17 Table</h2>
  <div class="slide-sub">Your subtitle here</div>
  <svg class="content" viewBox="0 0 350 195">
    <rect x="0" y="0" width="350" height="8" fill="var(--slate)"/>
    <g fill="var(--light)"><rect x="30" y="10" width="100" height="80"/><rect x="135" y="10" width="100" height="80"/><rect x="240" y="10" width="110" height="80"/><rect x="30" y="95" width="100" height="80"/><rect x="135" y="95" width="100" height="80"/><rect x="240" y="95" width="110" height="80"/></g>
    <g font-size="4.6"><text x="0" y="50">Row</text><text x="0" y="135">Row</text><text x="36" y="20">• Bullet text</text><text x="141" y="20">• Bullet text</text><text x="246" y="20">• Bullet text</text><text x="36" y="105">• Bullet text</text><text x="141" y="105">• Bullet text</text><text x="246" y="105">• Bullet text</text></g>
  </svg>
  <div class="strapline">A strapline may be placed here</div>
  <div class="brand-mini"><i></i>Corvane</div>
</section>

<!-- 1 Textboxes -->
<section class="slide">
  <div class="slide-no">30</div>
  <h2 class="slide-title">1 Textboxes</h2>
  <div class="slide-sub">Description</div>
  <svg class="content" viewBox="0 0 350 195">
    <g font-size="4.6">
      <text x="60" y="8" fill="var(--olive)" text-anchor="end">Quote</text>
      <text x="60" y="28" text-anchor="end">Standard text</text><text x="60" y="34" text-anchor="end">summary</text>
      <text x="70" y="22">Standard text</text><text x="70" y="28" font-weight="600">Regular bold text</text><text x="70" y="34">• Bullet</text><text x="76" y="40">– Sub bullet</text>
      <text x="60" y="60" text-anchor="end">Bold heading</text><text x="70" y="60" font-weight="600">Heading</text>
      <text x="60" y="82" text-anchor="end">Data heading</text><text x="60" y="88" text-anchor="end">summary</text>
      <rect x="70" y="100" width="55" height="8" fill="var(--light)"/><text x="73" y="106">Callout box</text>
      <text x="60" y="106" fill="var(--olive)" text-anchor="end">Callout text</text>
      <text x="60" y="122" fill="var(--olive)" text-anchor="end">Source note</text><text x="60" y="132" fill="var(--olive)" text-anchor="end">Footnote</text>
      <text x="60" y="142" fill="var(--olive)" text-anchor="end">Label</text><text x="60" y="152" fill="var(--olive)" text-anchor="end">Caption</text>
      <text x="200" y="8" fill="var(--olive)">Quote</text>
      <rect x="240" y="2" width="110" height="26" fill="var(--pale)"/><text x="244" y="10">"A quote line set in italic-free</text><text x="244" y="17">narrow text for statements"</text>
      <text x="210" y="44" fill="var(--olive)">Titled text</text><text x="250" y="44" font-weight="600">Standard bold text</text><text x="250" y="52">Standard text</text><text x="250" y="60">• Bullet</text><text x="256" y="67">– Sub bullet</text><text x="262" y="74">· Sub-sub bullet</text>
    </g>
  </svg>
  <div class="brand-mini"><i></i>Corvane</div>
</section>

</main>
</body>
</html>
```